Providing Back Office Solutions to Financial Advisors and Attorney Needs a Business Card Design

Need a Business Card Design that speaks to Financial Advisor and Attorneys. Some of the word that come to mind is Clean/Simple & Futuristic.

Industry/Entity Type

Business

```html
<!DOCTYPE html>
<html lang="en">
<head>
<meta charset="utf-8">
<title>Norvane Back Office Solutions – Business Card</title>
<link href="https://fonts.googleapis.com/css2?family=Open+Sans:wght@400;600&display=swap" rel="stylesheet">
<style>
  :root{
    --backdrop:#d9d9db;
    --card:#1b1c1e;
    --card-edge:#26272a;
    --brand-blue:#2a7fbd;
    --text-light:#e9e9ea;
    --text-muted:#8c8f94;
    --rule:#6b6e73;
  }
  *{margin:0;padding:0;box-sizing:border-box}
  html,body{width:1200px;height:864px;overflow:hidden}
  body{background:var(--backdrop);font-family:"Open Sans",Arial,sans-serif;position:relative}

  .card{position:absolute;width:560px;height:320px;background:var(--card);border:1px solid var(--card-edge);border-radius:4px;box-shadow:0 10px 30px rgba(0,0,0,.25)}
  .card--front{left:50px;top:90px}
  .card--back{left:590px;top:454px}

  .wordmark{display:flex;align-items:center;gap:14px}
  .wordmark__square{width:56px;height:56px;background:var(--brand-blue)}
  .wordmark__divider{width:1px;height:92px;background:var(--rule)}
  .wordmark__name{font-size:50px;font-weight:400;color:var(--brand-blue);letter-spacing:3px;line-height:1}
  .wordmark__tagline{font-size:13px;font-weight:400;color:var(--brand-blue);letter-spacing:.5px;margin-top:6px}

  .card--front .wordmark{position:absolute;left:80px;top:92px}
  .front__web{position:absolute;left:98px;top:218px;font-size:14px;letter-spacing:5px;color:var(--text-muted)}

  .card--back .wordmark{position:absolute;right:30px;top:54px;gap:10px}
  .card--back .wordmark__square{width:42px;height:42px}
  .card--back .wordmark__divider{height:70px}
  .card--back .wordmark__name{font-size:38px}
  .card--back .wordmark__tagline{font-size:10px}

  .person{position:absolute;left:26px;top:34px}
  .person__name{font-size:15px;font-weight:600;color:var(--brand-blue);letter-spacing:.5px}
  .person__title{font-size:11px;color:var(--text-muted);margin-top:2px}

  .contacts{position:absolute;left:26px;top:96px;list-style:none}
  .contacts li{display:flex;align-items:center;gap:8px;font-size:12.5px;color:var(--text-light);line-height:18px}
  .contacts svg{width:11px;height:11px;fill:var(--brand-blue)}

  .back__rule{position:absolute;left:26px;right:28px;top:190px;height:1px;background:var(--rule)}
  .address{position:absolute;right:28px;top:212px;text-align:right;font-size:14px;color:var(--text-light);line-height:20px}
  .address__web{letter-spacing:3px}
</style>
</head>
<body>

<section class="card card--front">
  <div class="wordmark">
    <div class="wordmark__square"></div>
    <div class="wordmark__divider"></div>
    <div>
      <div class="wordmark__name">NORVANE</div>
      <div class="wordmark__tagline">BACK OFFICE SOLUTIONS</div>
    </div>
  </div>
  <div class="front__web">www.norvane.com</div>
</section>

<section class="card card--back">
  <div class="person">
    <div class="person__name">DANIEL REYES</div>
    <div class="person__title">CEO/FOUNDER</div>
  </div>

  <ul class="contacts">
    <li><svg viewBox="0 0 12 12"><path d="M2 1h3l1 3-1.5 1a7 7 0 0 0 2.5 2.5L8 6l3 1v3a1 1 0 0 1-1 1A9 9 0 0 1 1 2a1 1 0 0 1 1-1z"/></svg>555 210 4471</li>
    <li><svg viewBox="0 0 12 12"><path d="M3.5 0h5a1 1 0 0 1 1 1v10a1 1 0 0 1-1 1h-5a1 1 0 0 1-1-1V1a1 1 0 0 1 1-1zm0 1.5v7.5h5V1.5z"/></svg>555 382 9016</li>
    <li><svg viewBox="0 0 12 12"><path d="M3 0h5v3H3zM1 4h10v6H9v2H3v-2H1zm3 4v3h4V8z"/></svg>555 647 1123</li>
    <li><svg viewBox="0 0 12 12"><path d="M0 2h12v8H0zm1 1v.5l5 3 5-3V3z"/></svg>daniel@norvane.com</li>
  </ul>

  <div class="wordmark">
    <div class="wordmark__square"></div>
    <div class="wordmark__divider"></div>
    <div>
      <div class="wordmark__name">NORVANE</div>
      <div class="wordmark__tagline">BACK OFFICE SOLUTIONS</div>
    </div>
  </div>

  <div class="back__rule"></div>

  <address class="address" style="font-style:normal">
    1420 Harbor View Road<br>
    Juneau, Alaska 99801<br>
    <span class="address__web">www.norvane.com</span>
  </address>
</section>

</body>
</html>
```